Tech Savy small Business accountant business card design

We need a business card for a new company based in the cloud. We provide tax, business advisory, accounting, information technology solutions and back office functions to small businesses. We offer fixed fee packages with add on services as you need them. By harnessing technology we simplify small business operational processes providing valuable time and information for small business owners to grow their business. In the logo (zulvarine) we want to be able to see zulv and experts. The final design should communicate achieving growth dreams and balance (ie life and $).
Updates
This project has been temporarily placed on hold until I finalize "Tech Savy small Business accountant needs a logo". I invite all designers to submit on this logo project. Once my logo is finalized I will resume this business card contest. Thanks Added Wednesday, March 19, 2014
This project has been temporarily placed on hold until I finalize "Tech Savy small Business accountant logo". I invite all designers to submit on this logo project. Once my logo is finalized I will resume this business card contest. Thanks Added Thursday, March 20, 2014
Target Market(s)
Small Business (Revenue $500,000, more than 3 employees) owners.
Industry/Entity Type
Small Business
Contact Information for Business Card
Marla Pennick (Principal)
Accountant, Tax Agent.
TEL | 0417 583 916
EMAIL | Marla.Pennick@zulvarine.com.au
WEB | www.zulvarine.com.au
Look and feel

```html
<!DOCTYPE html>
<html lang="en">
<head>
<meta charset="utf-8">
<title>zulvarine business card</title>
<link rel="stylesheet" href="https://fonts.googleapis.com/css2?family=Open+Sans:wght@400;600;700&display=swap">
<style>
  :root {
    --page: #eceff2;
    --card: #ffffff;
    --blue: #1f8fd6;
    --blue-deep: #1872c0;
    --blue-pale: #cfe6f6;
    --grey: #7d7f84;
    --grey-light: #e3e5e8;
    --shadow: rgba(20, 40, 60, 0.18);
  }
  * { box-sizing: border-box; margin: 0; padding: 0; }
  html, body { width: 1200px; height: 913px; overflow: hidden; }
  body {
    background: var(--page);
    font-family: "Open Sans", Arial, sans-serif;
    position: relative;
  }
  .card {
    position: absolute;
    width: 560px;
    height: 320px;
    background: var(--card);
    border-radius: 18px;
    overflow: hidden;
    box-shadow: 0 10px 30px var(--shadow);
  }
  .card--front { left: 70px; top: 110px; }
  .card--back { left: 570px; top: 480px; }
  .card__art { position: absolute; inset: 0; width: 100%; height: 100%; }

  .brand { position: absolute; }
  .brand__name {
    font-weight: 700;
    color: var(--blue);
    line-height: 1;
    letter-spacing: -0.5px;
  }
  .brand__tagline { color: var(--grey); font-weight: 400; }

  .card--front .brand { left: 282px; top: 24px; }
  .card--front .brand__name { font-size: 42px; }
  .card--front .brand__tagline { font-size: 12.5px; margin-top: 4px; }

  .card--back .brand { left: 0; right: 0; top: 112px; text-align: center; }
  .card--back .brand__name { font-size: 62px; }
  .card--back .brand__tagline { font-size: 17px; margin-top: 6px; }

  .person {
    position: absolute;
    right: 34px;
    top: 100px;
    text-align: right;
  }
  .person__name { font-size: 18px; font-weight: 700; color: var(--blue); text-transform: uppercase; }
  .person__name span { text-transform: none; }
  .person__role { font-size: 12px; color: var(--grey); margin-top: 1px; }

  .contacts {
    position: absolute;
    right: 34px;
    top: 150px;
    list-style: none;
    text-align: right;
  }
  .contacts__item {
    font-size: 12px;
    color: var(--blue);
    line-height: 19px;
    display: flex;
    justify-content: flex-end;
    align-items: center;
    gap: 8px;
  }
  .contacts__icon { width: 12px; height: 12px; fill: none; stroke: var(--grey); stroke-width: 1.6; }
</style>
</head>
<body>

<section class="card card--front" aria-label="Business card front">
  <svg class="card__art" viewBox="0 0 560 320" aria-hidden="true">
    <defs>
      <linearGradient id="band" x1="0" y1="0" x2="1" y2="1">
        <stop offset="0" stop-color="#4aa9e3"/>
        <stop offset="1" stop-color="#1872c0"/>
      </linearGradient>
    </defs>
    <circle cx="520" cy="40" r="95" fill="var(--blue-pale)" opacity="0.55"/>
    <polygon points="0,40 60,40 150,300 40,320 0,320" fill="var(--grey-light)"/>
    <polygon points="150,0 240,0 296,216 560,262 560,320 235,268" fill="url(#band)"/>
  </svg>

  <div class="brand">
    <div class="brand__name">zulvarine</div>
    <div class="brand__tagline">Your business and accounting partner</div>
  </div>

  <div class="person">
    <div class="person__name">Marla Pennick <span>(Principal)</span></div>
    <div class="person__role">Accountant, Tax Agent</div>
  </div>

  <ul class="contacts">
    <li class="contacts__item">0417 583 916
      <svg class="contacts__icon" viewBox="0 0 12 12"><path d="M2 1.5 L4 1.5 L5 4 L3.8 5 Q5 7.5 7 8.2 L8 7 L10.5 8 L10.5 10 Q6 11 3 7.5 Q1 5 2 1.5 Z"/></svg>
    </li>
    <li class="contacts__item">www.zulvarine.com.au
      <svg class="contacts__icon" viewBox="0 0 12 12"><circle cx="6" cy="6" r="4.8"/><ellipse cx="6" cy="6" rx="2" ry="4.8"/><line x1="1.2" y1="6" x2="10.8" y2="6"/></svg>
    </li>
    <li class="contacts__item">Marla.Pennick@zulvarine.com.au
      <svg class="contacts__icon" viewBox="0 0 12 12"><rect x="1" y="2.5" width="10" height="7"/><polyline points="1,2.5 6,6.5 11,2.5"/></svg>
    </li>
  </ul>
</section>

<section class="card card--back" aria-label="Business card back">
  <svg class="card__art" viewBox="0 0 560 320" aria-hidden="true">
    <circle cx="40" cy="290" r="130" fill="var(--blue-pale)" opacity="0.7"/>
  </svg>
  <div class="brand">
    <div class="brand__name">zulvarine</div>
    <div class="brand__tagline">Your business and accounting partner</div>
  </div>
</section>

</body>
</html>
```